Napa Winery Zinfandel label

We are a new start-up winery of high-end Napa wine. The label is to be silk screened or etched into the bottle. This initial logo is for the Velvet Ember Wine Co. Zinfandel wine.

The attached is an idea I would like followed for general guidance, meant to depict a "carnal sin" and sensual as per attached image.

Looking for some new ideas.....subtle sexy but risqué preferred! Silhouette in white and red writing of "Velvet zin" is what we are hoping for....

Please depict on a wine bottle (red wine) or near black background.

Thank you.

Font styles to use
Other font styles liked:
• colonna mt

Colors
f04950
ffffff

Requirements
Must have
• Female silhouette - risqué
Nice to have
• sensual - edgy
Should not have
• gold

```html
<!DOCTYPE html>
<html lang="en">
<head>
<meta charset="utf-8">
<title>Velvet Ember Wine Co. – Zinfandel Label</title>
<link rel="stylesheet" href="https://fonts.googleapis.com/css2?family=Italiana&family=Marcellus&display=swap">
<style>
  :root {
    --bg: #0b0a0b;
    --bg-glow: #1a1718;
    --title-white: #ffffff;
    --title-red: #f04950;
    --figure-deep: #3a1a2a;
    --figure-mid: #8a3a5a;
    --figure-soft: #c98ab8;
    --info: #e6ecc2;
    --info-light: #f2f2ea;
  }
  * { margin: 0; padding: 0; box-sizing: border-box; }
  html, body {
    width: 1111px;
    height: 1200px;
    overflow: hidden;
    background: var(--bg);
  }
  .label {
    position: relative;
    width: 1111px;
    height: 1200px;
    background: radial-gradient(ellipse at 50% 45%, var(--bg-glow) 0%, var(--bg) 70%);
  }
  .figure-art {
    position: absolute;
    left: 430px;
    top: 120px;
    width: 260px;
    height: 700px;
    border-radius: 130px 130px 70px 70px;
    background:
      radial-gradient(ellipse at 50% 12%, var(--figure-soft) 0%, rgba(201,138,184,0) 30%),
      linear-gradient(180deg, var(--figure-mid) 0%, var(--figure-deep) 70%, rgba(11,10,11,0) 100%);
    opacity: 0.7;
  }
  .wordmark {
    position: absolute;
    left: 0;
    width: 100%;
    text-align: center;
    font-family: "Italiana", serif;
    line-height: 1;
  }
  .wordmark-first {
    top: 330px;
    font-size: 118px;
    padding-right: 40px;
    color: var(--title-white);
    font-weight: 400;
  }
  .wordmark-second {
    top: 450px;
    font-size: 108px;
    padding-left: 50px;
    color: var(--title-red);
  }
  .winery {
    position: absolute;
    top: 880px;
    width: 100%;
    text-align: center;
    font-family: "Marcellus", serif;
    font-size: 40px;
    color: var(--info);
    letter-spacing: 1px;
  }
  .varietal,
  .vintage {
    position: absolute;
    width: 100%;
    text-align: center;
    font-family: "Marcellus", serif;
    font-size: 24px;
    color: var(--info-light);
    letter-spacing: 1px;
  }
  .varietal { top: 945px; }
  .vintage { top: 1045px; }
</style>
</head>
<body>
  <main class="label">
    <div class="figure-art" role="img" aria-label="Female silhouette in white and red line art, head tilted back, shown from the side"></div>
    <h1 class="wordmark wordmark-first">Velvet</h1>
    <p class="wordmark wordmark-second">zin</p>
    <p class="winery">Velvet Ember Wine Co.</p>
    <p class="varietal">ZINFANDEL VINE</p>
    <p class="vintage">NAPA VALLEY 2015</p>
  </main>
</body>
</html>
```